A land page lead collector for people who want to reduce there postage costs

We are looking to create a single page website landing page to collect leads of people who want to reduce there postage costs.

The form should basically ask:

Name:
Business Name:
Address:
Town:
Post Code:
Email:
Phone:
Letter Volume Per Week:
Parcel Volume Per Week:

We should basically be advertising cheaper postage costs.

We will not be showing prices on this website we will just be collecting the leads.

Our competition website is as follows https://mailfernquest.com

But we are not a online service. This is just a collector to get leads of people who want to save money on there postage costs.
Updates

Target Market(s)

Small and medium sized enterprises

Industry/Entity Type

Advertising

Number of Pages Required

1 page

Colors
ec2027
0356a4

Requirements
Must have
• Form above the fold of the page
Nice to have
• Colour red and blue.
• Parallax design would be nice.

```html
<!DOCTYPE html>
<html lang="en">
<head>
<meta charset="utf-8">
<title>Company name – Cheaper Postage</title>
<link href="https://fonts.googleapis.com/css2?family=Roboto:wght@300;400;500;700&display=swap" rel="stylesheet">
<style>
:root{
  --red:#ec2027;
  --blue:#0356a4;
  --sand-top:#ccaa76;
  --sand-mid:#b18446;
  --sand-deep:#9c6a2c;
  --ink:#2a1c0c;
  --footer:#2a1c0a;
  --footer-text:#d8b77e;
  --white:#ffffff;
  --icon-brown:#4a3214;
}
*{box-sizing:border-box;margin:0;padding:0}
html,body{width:1108px;height:1200px;overflow:hidden}
body{font-family:"Roboto",Arial,sans-serif;color:var(--ink)}
.page{position:relative;width:1108px;height:1200px;overflow:hidden;
  background:linear-gradient(180deg,var(--sand-top) 0%,var(--sand-mid) 38%,var(--sand-deep) 60%,#a2702f 68%)}
.abs{position:absolute}

/* header */
.brand{left:95px;top:27px;font-size:21px;font-weight:500}
.brand span{font-weight:400}
.call{left:695px;top:14px;font-size:20px}
.call b{font-weight:700}
.social{display:flex;align-items:center;gap:6px;font-size:11.5px}
.social i{display:block;width:20px;height:20px;border-radius:50%;background:#7aa7e6;border:2px solid #dfe9f7}
.social i + i{background:#5cc3ec}
.social-top{left:879px;top:15px}
.nav{display:flex;font-size:11.5px}
.nav a{color:inherit;text-decoration:none}
.nav .sep{margin:0 12px;color:inherit}
.nav .current{font-weight:700}
.nav-top{right:102px;top:47px}

/* hero */
.band{height:53px}
.band.blue{background:var(--blue)}
.band.red{background:var(--red)}
.stamp{left:92px;top:81px;width:916px;height:480px}
.cargo-icon{left:166px;top:245px;width:181px;height:154px;border-radius:8px;
  background:radial-gradient(circle at 40% 60%,var(--icon-brown),rgba(74,50,20,.75))}
.headline{left:364px;top:246px;color:var(--white);line-height:1}
.headline .light{font-weight:300;font-size:38px;display:block;margin-bottom:4px}
.headline .strong{font-weight:700;font-size:40px;display:block;margin-top:6px}

.lead-form{left:718px;top:109px;width:267px;height:425px;background:var(--red);padding:21px 26px 0}
.lead-form h2{font-size:12px;font-weight:400;color:var(--white);margin-bottom:5px}
.lead-form .field{display:block;width:211px;height:30px;margin-bottom:6.9px;background:var(--white);
  border:1px solid #c9c9c9;border-radius:3px;font:400 12.5px "Roboto",Arial,sans-serif;color:#444;padding:0 11px;line-height:28px}
.lead-form .submit{position:absolute;left:118px;top:377px;width:119px;height:30px;background:#000;color:var(--white);
  font:700 14px "Roboto",Arial,sans-serif;border:0;border-radius:3px;letter-spacing:.3px}

/* features */
.feature{top:594px}
.feature h3{font-size:37px;font-weight:300;letter-spacing:-.5px;margin-bottom:8px;line-height:1.1}
.feature h3 b{font-weight:700}
.feature p{font-size:11.6px;line-height:16.6px;color:#3a2810}
.more{position:absolute;top:175px;left:0;width:83px;height:21px;background:var(--red);color:var(--white);
  font-size:9.5px;font-weight:700;text-align:center;line-height:21px}

/* customers */
.customers{left:0;top:814px;width:1108px;height:232px;
  background:linear-gradient(120deg,#b48a52 0%,#c19a63 30%,#a87d44 55%,#bf9860 80%,#ab7f47 100%)}
.customers h2{position:absolute;top:34px;width:100%;text-align:center;font-size:37px;font-weight:300;letter-spacing:-.5px}
.customers h2 b{font-weight:700}
.client{position:absolute;top:102px;width:151px;height:73px;background:rgba(240,228,214,.88);
  color:#8f7d69;font-size:15px;font-weight:300;display:flex;align-items:center;justify-content:center}

/* footer */
.footer{left:0;top:1046px;width:1108px;height:154px;background:var(--footer);color:var(--footer-text)}
.nav-foot{position:absolute;left:0;width:100%;justify-content:center;top:24px}
.address{position:absolute;left:92px;top:79px;font-size:10.3px;line-height:16px;font-style:normal}
.address b{font-size:11px}
.social-foot{position:absolute;right:102px;top:81px}
.copy{position:absolute;right:10px;top:111px;font-size:10.3px}
</style>
</head>
<body>
<div class="page">

  <header>
    <div class="abs brand">Company name <span>(logo)</span></div>
    <div class="abs call">Call: <b>0100 5550 42</b></div>
    <div class="abs social social-top">meet us online <i></i><i></i></div>
    <nav class="abs nav nav-top">
      <a class="current" href="#">Home</a><span class="sep">|</span>
      <a href="#">About us</a><span class="sep">|</span>
      <a href="#">Pricing</a><span class="sep">|</span>
      <a href="#">Geta an Account</a><span class="sep">|</span>
      <a href="#">Login</a><span class="sep">|</span>
      <a href="#">Contact Us</a>
    </nav>
  </header>

  <section class="hero">
    <div class="abs band blue" style="left:0;top:253px;width:92px"></div>
    <div class="abs band red" style="left:0;top:306px;width:92px"></div>
    <div class="abs band blue" style="left:1008px;top:253px;width:100px"></div>
    <div class="abs band red" style="left:1008px;top:306px;width:100px"></div>

    <svg class="abs stamp" viewBox="0 0 916 480" aria-hidden="true">
      <defs>
        <pattern id="edge-top" width="18" height="12" patternUnits="userSpaceOnUse">
          <path d="M0 1 H4 A5 5 0 0 0 14 1 H18" fill="none" stroke="#7a5428" stroke-width="1"/>
        </pattern>
        <pattern id="edge-bottom" width="18" height="12" patternUnits="userSpaceOnUse">
          <path d="M0 11 H4 A5 5 0 0 1 14 11 H18" fill="none" stroke="#7a5428" stroke-width="1"/>
        </pattern>
        <pattern id="edge-left" width="12" height="18" patternUnits="userSpaceOnUse">
          <path d="M1 0 V4 A5 5 0 0 1 1 14 V18" fill="none" stroke="#7a5428" stroke-width="1"/>
        </pattern>
        <pattern id="edge-right" width="12" height="18" patternUnits="userSpaceOnUse">
          <path d="M11 0 V4 A5 5 0 0 0 11 14 V18" fill="none" stroke="#7a5428" stroke-width="1"/>
        </pattern>
      </defs>
      <rect x="0" y="0" width="916" height="12" fill="url(#edge-top)"/>
      <rect x="0" y="468" width="916" height="12" fill="url(#edge-bottom)"/>
      <rect x="0" y="0" width="12" height="480" fill="url(#edge-left)"/>
      <rect x="904" y="0" width="12" height="480" fill="url(#edge-right)"/>
    </svg>

    <div class="abs cargo-icon" role="img" aria-label="Hand truck carrying a parcel"></div>

    <h1 class="abs headline">
      <span class="light">World Class</span>
      <span class="light">Service at</span>
      <span class="strong">Competitive rates</span>
    </h1>

    <form class="abs lead-form">
      <h2>Fill this form below to get more info</h2>
      <div class="field">Name</div>
      <div class="field">Business Name</div>
      <div class="field">Address</div>
      <div class="field">Town</div>
      <div class="field">Post Code</div>
      <div class="field">Email</div>
      <div class="field">Phone</div>
      <div class="field">Letter Volume Per Week</div>
      <div class="field">Parcel Volume Per Week</div>
      <button class="submit" type="button">SUBMIT</button>
    </form>
  </section>

  <section class="features">
    <article class="abs feature" style="left:92px;width:252px">
      <h3>Our <b>Services</b></h3>
      <p>Lorem ipsum dolor sit amet, consectetur adipiscing elit. Duis eu dignissim justo, sed commodo sem. Pellentesque lobortis, ipsum id euismod semper, dolor orci egestas risus, nec cursus orci quam eget enim. Nunc molestie pretium nisl vel ornare. Curabitur ultricies mi quis lacinia congue</p>
      <span class="more">More Info</span>
    </article>
    <article class="abs feature" style="left:424px;width:268px">
      <h3>Our <b>Pricing</b></h3>
      <p>Lorem ipsum dolor sit amet, consectetur adipiscing elit. Duis eu dignissim justo, sed commodo sem. Pellentesque lobortis, ipsum id euismod semper, dolor orci egestas risus, nec cursus orci quam eget enim. Nunc molestie pretium nisl vel ornare. Curabitur ultricies mi quis lacinia congue</p>
      <span class="more" style="left:2px">More Info</span>
    </article>
    <article class="abs feature" style="left:742px;width:268px">
      <h3>Our <b>Support</b></h3>
      <p>Lorem ipsum dolor sit amet, consectetur adipiscing elit. Duis eu dignissim justo, sed commodo sem. Pellentesque lobortis, ipsum id euismod semper, dolor orci egestas risus, nec cursus orci quam eget enim. Nunc molestie pretium nisl vel ornare. Curabitur ultricies mi quis lacinia congue</p>
      <span class="more">More Info</span>
    </article>
  </section>

  <section class="abs customers" role="img" aria-label="Faceted geometric background behind customer logos">
    <h2>Our <b>Customers</b></h2>
    <div class="client" style="left:106px">Logo</div>
    <div class="client" style="left:294px">Logo</div>
    <div class="client" style="left:480px">Logo</div>
    <div class="client" style="left:667px">Logo</div>
    <div class="client" style="left:854px">Logo</div>
  </section>

  <footer class="abs footer">
    <nav class="nav nav-foot">
      <a class="current" href="#">Home</a><span class="sep">|</span>
      <a href="#">About us</a><span class="sep">|</span>
      <a href="#">Pricing</a><span class="sep">|</span>
      <a href="#">Geta an Account</a><span class="sep">|</span>
      <a href="#">Login</a><span class="sep">|</span>
      <a href="#">Contact Us</a>
    </nav>
    <address class="address">
      <b>Company Name (Logo)</b><br>
      Dummy Addrsss, Cedar Hollow 214-555-0148 4820 Harlow Lane,<br>
      Suite 210-Fairview, TX 75099
    </address>
    <div class="social social-foot">meet us online <i></i><i></i></div>
    <div class="copy">@2015 Company Name, All rights reserved.</div>
  </footer>

</div>
</body>
</html>
```